I am looking for help designing my new business cards. I would like rounded edges and a raised logo on the back of the card. I have 2 Logos. One with a boat in it and one without. I'd like the one on the back to be the one that includes the boat and just the name on the front. I have included multiple formats of my logo. Please let me know if you need anymore.

Target Market(s)

Potential buyers and other sales brokers

Industry/Entity Type

Sales - Yacht / Boat Sales

Contact Information for Business Card

Id liike the front to include just the business name portion of the logo along with my name (Corwin Dalby), phone number (555.318.6027), website address (www.dalbymarineco.example) and not my physical address but just "Charleston, SC". The back should include my full logo that has the boat included. This portion I'd prefer raised amd take up the majority of the space there. Thanks!!

Colors
0054AA
0677BA
7BADD7
CADEEF
E8F1F8
0094D4
00A9DD
6FCCEA
C7EBF8
E9F6FB

Requirements
Must have
• Double sided
Nice to have
• My email address: Corwin@dalbymarineco.example The NMTG logo somewhere small on the front of the card
Should not have
• My full address, prefer only "Charleston, SC"

```html
<!DOCTYPE html>
<html lang="en">
<head>
<meta charset="utf-8">
<title>Dalby Marine Co — Business Card</title>
<link rel="stylesheet" href="https://fonts.googleapis.com/css2?family=Michroma&family=Poppins:wght@300;400&display=swap">
<style>
  :root {
    --stage: #2b2b2d;
    --card-white: #ffffff;
    --navy: #0c2d6b;
    --navy-back: #0b2a66;
    --ink: #1a1a1a;
    --rule: #9a9a9a;
  }
  * { margin: 0; padding: 0; box-sizing: border-box; }
  html, body { width: 1200px; height: 1108px; overflow: hidden; }
  body {
    background: var(--stage);
    display: flex;
    align-items: center;
    justify-content: center;
    gap: 60px;
  }
  .card {
    width: 400px;
    height: 660px;
    border-radius: 26px;
    position: relative;
    overflow: hidden;
  }
  .card--front {
    background: var(--card-white);
    display: flex;
    flex-direction: column;
    align-items: center;
    padding: 110px 36px 0;
  }
  .wordmark {
    font-family: "Michroma", sans-serif;
    color: var(--navy);
    font-size: 30px;
    letter-spacing: 2px;
    text-align: center;
    line-height: 1.25;
  }
  .holder-name {
    font-family: "Michroma", sans-serif;
    color: var(--navy);
    font-size: 21px;
    letter-spacing: 2px;
    margin-top: 190px;
  }
  .icon-rule {
    display: flex;
    align-items: center;
    width: 300px;
    margin-top: 18px;
    gap: 8px;
  }
  .icon-rule .line { flex: 1; height: 1px; background: var(--rule); }
  .icon-set { display: flex; gap: 6px; }
  .icon-set svg { width: 30px; height: 30px; display: block; }
  .contact {
    font-family: "Poppins", sans-serif;
    font-weight: 300;
    color: var(--ink);
    font-size: 17px;
    text-align: center;
    line-height: 1.55;
    margin-top: 10px;
  }
  .contact .domain { color: var(--navy); }
  .contact-rule { width: 300px; height: 1px; background: var(--rule); margin-top: 10px; }
  .city {
    font-family: "Poppins", sans-serif;
    font-weight: 300;
    color: var(--ink);
    font-size: 18px;
    margin-top: 12px;
  }
  .card--back { background: var(--navy-back); }
  .back-pattern { position: absolute; inset: 0; background: var(--navy-back); }
  .back-wordmark {
    position: absolute;
    left: 0; right: 0;
    top: 430px;
    text-align: center;
    font-family: "Michroma", sans-serif;
    color: #ffffff;
    font-size: 22px;
    letter-spacing: 2px;
    line-height: 1.3;
  }
</style>
</head>
<body>
  <section class="card card--front" aria-label="Card front">
    <div class="wordmark">DALBY<br>MARINE CO</div>
    <div class="holder-name">CORWIN DALBY</div>
    <div class="icon-rule">
      <span class="line"></span>
      <div class="icon-set">
        <svg viewBox="0 0 30 30" aria-label="Phone"><rect width="30" height="30" rx="5" fill="#0c2d6b"/><path d="M10 8c1.5-1 2.5-.5 3 1l1 2.5c.3 1-.5 1.6-1.2 2 .8 1.8 2 3 3.7 3.8.4-.7 1-1.5 2-1.2l2.5 1c1.5.5 2 1.5 1 3-1.2 1.8-3 2-5 1.2-3.5-1.5-6-4-7.6-7.5C8.6 11 8.6 9 10 8z" fill="#fff"/></svg>
        <svg viewBox="0 0 30 30" aria-label="Email"><rect width="30" height="30" rx="5" fill="#0c2d6b"/><rect x="7" y="9.5" width="16" height="11" fill="none" stroke="#fff" stroke-width="1.6"/><path d="M7 9.5l8 6.5 8-6.5" fill="none" stroke="#fff" stroke-width="1.6"/></svg>
        <svg viewBox="0 0 30 30" aria-label="Website"><rect width="30" height="30" rx="5" fill="#0c2d6b"/><circle cx="15" cy="15" r="7.5" fill="none" stroke="#fff" stroke-width="1.6"/><ellipse cx="15" cy="15" rx="3.2" ry="7.5" fill="none" stroke="#fff" stroke-width="1.3"/><path d="M7.5 15h15" stroke="#fff" stroke-width="1.3"/></svg>
      </div>
      <span class="line"></span>
    </div>
    <div class="contact">
      555.318.6027<br>
      Corwin@dalbymarineco.example<br>
      www.<span class="domain">dalbymarineco</span>.example
    </div>
    <div class="contact-rule"></div>
    <div class="city">Charleston, SC</div>
  </section>

  <section class="card card--back" aria-label="Card back">
    <div class="back-pattern" role="img" aria-label="Raised tone-on-tone repeating wordmark pattern in navy"></div>
    <div class="back-wordmark">DALBY<br>MARINE CO</div>
  </section>
</body>
</html>
```